Tasman Curdworks Guild needs new business cards

We need new business cards designed and produced. We are likely to need other design work done for ads, flyers etc in future.

We would like to start with an initial business card.

The Tasman Curdworks Guild (TCG) is a membership-based not-for-profit organisation that looks after the interests of Australia's small to medium artisan cheesemakers, many of whom are also small-scale farmers. The design should be simple, using our logo, but also communicate our artisan cheese and small dairy farm focus.

The first card to be designed and produced is for me, Miriam Tolhurst. My details are:

Miriam Tolhurst
Secretary
Tasman Curdworks Guild (TCG)
http://www.curdworksguild.example
T +61452837190
E miriam.miriamtolhurst@mailbox.example

I have attached the TCG logo in jpg form. I have a higher resolution version available if needed.

Thank you!

Miriam

Miriam Tolhurst
Tasman Curdworks Guild
miriam.miriamtolhurst@mailbox.example
+61452837190

Sans Serif

• Logo (see attached file)

```html
<!DOCTYPE html>
<html lang="en">
<head>
<meta charset="utf-8">
<title>Tasman Curdworks Guild – Business Card</title>
<link rel="stylesheet" href="https://fonts.googleapis.com/css2?family=Gilda+Display&display=swap">
<style>
  :root {
    --cheese: #fcc96a;
    --paper: #ffffff;
    --rind: #5a3418;
    --stage: #ece8e1;
    --card-w: 700px;
    --card-h: 400px;
  }
  * { box-sizing: border-box; margin: 0; padding: 0; }
  html, body { width: 1200px; height: 892px; overflow: hidden; }
  body {
    background: var(--stage);
    font-family: "Gilda Display", Georgia, serif;
    display: flex; flex-direction: column; align-items: center; justify-content: center; gap: 32px;
  }
  .card {
    position: relative; width: var(--card-w); height: var(--card-h);
    overflow: hidden; box-shadow: 0 6px 18px rgba(0,0,0,.18);
  }
  .card-art { position: absolute; inset: 0; }

  /* Front */
  .card--front { background: var(--cheese); }
  .front-mark {
    position: absolute; left: 120px; top: 0; height: 100%;
    display: flex; align-items: center; gap: 34px;
  }
  .mark-circle {
    flex: none; border-radius: 50%;
    background: var(--cheese); border: 3px solid var(--rind);
  }
  .front-mark .mark-circle { width: 150px; height: 150px; }
  .front-name {
    color: var(--rind); font-size: 50px; line-height: 1.05; font-weight: 400;
  }

  /* Back */
  .card--back { background: var(--paper); }
  .back-content { position: absolute; left: 110px; top: 62px; right: 60px; }
  .person-name { color: var(--paper); font-size: 48px; font-weight: 400; text-align: right; padding-right: 30px; }
  .person-role { color: var(--rind); font-size: 22px; text-align: right; padding-right: 120px; margin-top: 2px; }
  .org-name { color: var(--rind); font-size: 19px; line-height: 1.25; margin-top: 10px; }
  .contact-list { list-style: none; margin-top: 10px; }
  .contact-list li {
    display: flex; align-items: center; gap: 12px;
    color: var(--paper); font-size: 16px; line-height: 1.6;
  }
  .contact-icon { width: 18px; height: 18px; flex: none; }
  .back-mark {
    position: absolute; right: 56px; bottom: 34px;
    display: flex; align-items: center; gap: 14px;
  }
  .back-mark .mark-circle { width: 70px; height: 70px; }
  .back-mark-name { color: var(--rind); font-size: 22px; }
</style>
</head>
<body>

<section class="card card--front" aria-label="Card front">
  <svg class="card-art" viewBox="0 0 700 400" aria-hidden="true">
    <path fill="#ffffff" d="M70 70 C150 50 200 80 280 55 C370 30 450 70 540 50 C590 40 620 60 630 90 C640 160 620 230 640 300 C650 340 610 355 560 345 C470 330 400 360 300 340 C220 325 150 355 90 340 C55 330 60 290 65 250 C75 190 50 130 70 70 Z"/>
    <g fill="#ffffff">
      <circle cx="30" cy="25" r="6"/><circle cx="655" cy="30" r="8"/><circle cx="672" cy="70" r="4"/>
      <circle cx="25" cy="200" r="5"/><circle cx="40" cy="370" r="7"/><circle cx="665" cy="360" r="11"/>
      <circle cx="620" cy="385" r="5"/><circle cx="350" cy="380" r="4"/><circle cx="200" cy="22" r="5"/>
    </g>
    <g fill="#fcc96a">
      <circle cx="560" cy="90" r="7"/><circle cx="100" cy="310" r="5"/>
    </g>
  </svg>
  <div class="front-mark">
    <span class="mark-circle"></span>
    <h1 class="front-name">Tasman<br>Curdworks<br>Guild</h1>
  </div>
</section>

<section class="card card--back" aria-label="Card back">
  <svg class="card-art" viewBox="0 0 700 400" aria-hidden="true">
    <path fill="#fcc96a" d="M70 50 C160 35 240 60 340 40 C430 25 520 55 610 45 C650 42 660 70 650 110 C640 170 665 230 650 290 C640 330 600 335 540 330 C450 322 380 345 290 335 C200 325 130 345 80 330 C50 320 55 280 60 230 C65 170 40 110 70 50 Z"/>
    <g fill="#fcc96a">
      <circle cx="30" cy="30" r="5"/><circle cx="680" cy="25" r="6"/><circle cx="25" cy="150" r="4"/>
      <circle cx="40" cy="360" r="6"/><circle cx="675" cy="200" r="5"/><circle cx="300" cy="375" r="7"/>
      <circle cx="420" cy="385" r="4"/><circle cx="180" cy="20" r="4"/><circle cx="520" cy="15" r="5"/>
    </g>
    <g fill="#ffffff">
      <circle cx="620" cy="90" r="6"/><circle cx="95" cy="300" r="5"/><circle cx="380" cy="60" r="4"/>
    </g>
  </svg>
  <div class="back-content">
    <h1 class="person-name">Miriam Tolhurst</h1>
    <p class="person-role">Secretary</p>
    <p class="org-name">Tasman Curdworks<br>Guild (TCG)</p>
    <ul class="contact-list">
      <li>
        <svg class="contact-icon" viewBox="0 0 20 20" aria-hidden="true"><circle cx="10" cy="10" r="9.5" fill="#5a3418"/><path d="M7 5.5l2 2-1 1.2c.6 1.4 1.7 2.5 3.1 3.1l1.2-1 2 2-1.3 1.5C9.6 14 6 10.4 5.7 7z" fill="#fcc96a"/></svg>
        +61452837190
      </li>
      <li>
        <svg class="contact-icon" viewBox="0 0 20 20" aria-hidden="true"><circle cx="10" cy="10" r="9.5" fill="#5a3418"/><rect x="5" y="6.5" width="10" height="7" fill="none" stroke="#fcc96a" stroke-width="1.3"/><path d="M5 6.5l5 4 5-4" fill="none" stroke="#fcc96a" stroke-width="1.3"/></svg>
        miriam.miriamtolhurst@mailbox.example
      </li>
      <li>
        <svg class="contact-icon" viewBox="0 0 20 20" aria-hidden="true"><circle cx="10" cy="10" r="9.5" fill="#5a3418"/><circle cx="10" cy="10" r="5" fill="none" stroke="#fcc96a" stroke-width="1.2"/><path d="M5 10h10M10 5c-2.5 3-2.5 7 0 10M10 5c2.5 3 2.5 7 0 10" fill="none" stroke="#fcc96a" stroke-width="1"/></svg>
        www.curdworksguild.example
      </li>
    </ul>
  </div>
  <div class="back-mark">
    <span class="mark-circle"></span>
    <span class="back-mark-name">Tasman Curdworks Guild</span>
  </div>
</section>

</body>
</html>
```